Real Estate Managemene Company Needs Business Card Design

We have a logo design and just need business cards made now for our business. Please use PDF logo # 3.

Card with Information to be attached shortly.

The card is used for a real estate management company. We will need to add four other employees and their cards.

Industry/Entity Type

Real Estate

Contact Information for Business Card

Tariq Hamdan
President
3187 Thornwick Avenue
Suite C
Brookmere Falls, IL 60152
Phone 630.417.2286
Fax 630.417.2287
Cell 630.473.8062
vantorp@mailbreeze.net

Once design is approved we will have four other employees
Omar Hamdan
Operations Manager

Nadia Hamdan
Administrative Manager

Faz Hamdan
Principal

We would need to take out the cell # 630.473.8062 out for the remaining three cards.

Requirements
Must have
• Please use logo attached

```html
<!DOCTYPE html>
<html lang="en">
<head>
<meta charset="utf-8">
<title>Northgate Property Group – Business Card</title>
<link rel="stylesheet" href="https://fonts.googleapis.com/css2?family=Josefin+Sans:wght@300;400&family=Cormorant+Garamond:wght@500&display=swap">
<style>
  :root{
    --backdrop:#16181c;
    --navy-dark:#0c1422;
    --navy:#1a2436;
    --blue-bright:#1f56c4;
    --blue-mid:#1a46a0;
    --blue-deep:#12306e;
    --slate:#8c97a6;
    --panel-light:#eef1f5;
    --panel-shade:#dde2e9;
    --ink:#3b4350;
    --muted:#6f7b8f;
    --white:#f4f6fa;
  }
  html,body{margin:0;padding:0;width:1200px;height:800px;overflow:hidden;background:var(--backdrop);}
  body{font-family:"Josefin Sans",Arial,sans-serif;}
  .card{position:absolute;left:75px;top:100px;width:1050px;height:600px;overflow:hidden;
    background:linear-gradient(100deg,#223049 0%,var(--navy) 45%,var(--navy-dark) 100%);}
  .brand{position:absolute;left:80px;top:190px;width:420px;text-align:center;}
  .brand-name{font-weight:400;font-size:40px;letter-spacing:3px;color:var(--blue-bright);text-transform:uppercase;}
  .name-panel{position:absolute;left:555px;top:0;width:495px;height:150px;
    background:linear-gradient(180deg,#0a111d,#141c2b);}
  .person{position:absolute;right:60px;top:28px;text-align:right;color:var(--white);}
  .person-name{font-size:46px;line-height:1;}
  .first{font-family:"Josefin Sans",Arial,sans-serif;font-weight:300;}
  .last{font-family:"Cormorant Garamond",Georgia,serif;font-weight:500;}
  .person-role{font-size:22px;font-weight:300;color:var(--muted);margin-top:4px;margin-right:40px;}
  .contact-rail{position:absolute;left:545px;top:150px;width:70px;height:280px;background:var(--panel-shade);}
  .contact-panel{position:absolute;left:615px;top:130px;width:435px;height:300px;background:var(--panel-light);}
  .skyline{position:absolute;left:0;bottom:0;width:100%;height:170px;
    background:linear-gradient(180deg,rgba(205,212,222,0) 0%,rgba(205,212,222,.8) 100%);}
  .icon{position:absolute;left:567px;width:26px;height:26px;}
  .contact-text{position:absolute;left:655px;color:var(--ink);font-weight:300;font-size:20px;letter-spacing:.5px;}
  .band{position:absolute;height:40px;}
  .footer{position:absolute;left:0;top:470px;width:1050px;height:130px;background:linear-gradient(180deg,#141b28,#0f1520);}
  .footer-text{position:absolute;color:var(--muted);font-weight:300;font-size:18px;line-height:24px;white-space:nowrap;}
</style>
</head>
<body>
<main class="card">
  <div class="brand"><div class="brand-name">Northgate</div></div>

  <div class="name-panel">
    <div class="person">
      <div class="person-name"><span class="first">Tariq </span><span class="last">Hamdan</span></div>
      <div class="person-role">President</div>
    </div>
  </div>

  <div class="contact-rail"></div>
  <div class="contact-panel">
    <div class="skyline" role="img" aria-label="Faint city skyline illustration"></div>
  </div>

  <svg class="icon" style="top:180px" viewBox="0 0 26 26"><rect x="2" y="6" width="22" height="15" fill="#4a5466"/><path d="M2 6 L13 15 L24 6" fill="none" stroke="#dde2e9" stroke-width="2"/></svg>
  <svg class="icon" style="top:248px" viewBox="0 0 26 26"><path d="M7 3 L11 3 L12 9 L9 11 Q11 16 15 18 L17 15 L23 16 L23 20 Q22 24 17 23 Q5 19 3 8 Q3 3 7 3Z" fill="#4a5466"/></svg>
  <svg class="icon" style="top:320px" viewBox="0 0 26 26"><circle cx="13" cy="13" r="11" fill="#4a5466"/><path d="M8 7 Q12 9 10 13 Q7 14 8 18 M16 5 Q14 9 18 11 Q21 12 19 17" fill="none" stroke="#dde2e9" stroke-width="2"/></svg>

  <div class="contact-text" style="top:185px">vantorp@mailbreeze.net</div>
  <div class="contact-text" style="top:240px;line-height:26px">630.417.2286<br>630.473.8062</div>
  <div class="contact-text" style="top:325px">WWW.NORTHGATEPG.COM</div>

  <div class="band" style="left:0;top:390px;width:250px;background:var(--blue-bright)"></div>
  <div class="band" style="left:250px;top:390px;width:300px;background:var(--blue-mid)"></div>
  <div class="band" style="left:0;top:430px;width:120px;background:var(--blue-mid)"></div>
  <div class="band" style="left:120px;top:430px;width:200px;background:var(--blue-deep)"></div>
  <div class="band" style="left:320px;top:430px;width:300px;background:var(--blue-mid)"></div>
  <div class="band" style="left:550px;top:390px;width:80px;background:var(--blue-mid)"></div>
  <div class="band" style="left:620px;top:430px;width:300px;background:var(--blue-bright)"></div>
  <div class="band" style="left:920px;top:410px;width:130px;height:60px;background:var(--slate)"></div>

  <div class="footer">
    <div class="footer-text" style="left:30px;top:40px">3187 Thornwick Avenue<br>Suite C</div>
    <div class="footer-text" style="left:470px;top:70px">Brookmere Falls, IL 60152</div>
    <div class="footer-text" style="left:835px;top:90px">Fax 630.417.2287</div>
  </div>
</main>
</body>
</html>
```